Supplement Bottle Packaging and Design

We want to rebrand our current health supplements (see below). We do want it to be modern, vibrant and appealing supplement bottles. Very upscale and elegant as it targets primarily women.
NOTE: READ THE ATTACHED WORD DOCUMENT!
Bottle size: We are totally open to the bottle size and shape, as long it's a typical supplement bottle size to handle 90-120 capsules; what we mostly need is new bottle design/packaging. YOU DON’T HAVE TO USE THE CURRENT WHITE BOTTLE SHAPE, BUT ANYTHING MORE MODERN WOULD WORK!
Updates
We need more modern, clean sleek designs to choose from
Look and feel
Each slider illustrates characteristics of the customer's brand and the style your logo design should communicate.

```html
<!DOCTYPE html>
<html lang="en">
<head>
<meta charset="utf-8">
<title>Supplement Label Range</title>
<link rel="stylesheet" href="https://fonts.googleapis.com/css2?family=Bebas+Neue&display=swap">
<style>
  :root {
    --page-bg: #e6e6e6;
    --page-bg-top: #c4c4c4;
    --ink-white: #ffffff;
    --black-label: #141414;
    --clear-label: #c9a77a;
    --clear-label-dark: #a9865a;
    --lilac: #d9a6dc;
    --lilac-deep: #b57cc0;
    --peach: #f5a98a;
    --peach-deep: #e8805f;
  }
  * { margin: 0; padding: 0; box-sizing: border-box; }
  html, body { width: 1200px; height: 577px; overflow: hidden; }
  body {
    background: linear-gradient(180deg, var(--page-bg-top) 0%, var(--page-bg) 100%);
    font-family: "Bebas Neue", "Arial Narrow", sans-serif;
    position: relative;
  }
  .label {
    position: absolute;
    top: 196px;
    width: 196px;
    height: 258px;
    display: flex;
    flex-direction: column;
    color: var(--ink-white);
    text-align: center;
    box-shadow: 0 10px 18px rgba(0,0,0,0.12);
  }
  .label--clear { background: linear-gradient(135deg, var(--clear-label) 0%, var(--clear-label-dark) 100%); }
  .label--black { background: var(--black-label); }
  .label__head {
    flex: 1;
    display: flex;
    flex-direction: column;
    justify-content: flex-end;
    padding-bottom: 10px;
  }
  .label__name {
    font-size: 41px;
    line-height: 0.86;
    letter-spacing: 0.5px;
  }
  .label__claim {
    margin-top: 14px;
    font-size: 12px;
    line-height: 1.2;
    letter-spacing: 0.3px;
  }
  .label__band {
    height: 98px;
    display: flex;
    flex-direction: column;
    align-items: center;
    justify-content: center;
    gap: 10px;
  }
  .label__band--lilac { background: linear-gradient(90deg, var(--lilac-deep) 0%, var(--lilac) 45%, var(--lilac) 100%); }
  .label__band--peach { background: linear-gradient(90deg, var(--peach-deep) 0%, var(--peach) 45%, var(--peach) 100%); }
  .label__emblem {
    width: 44px;
    height: 32px;
    border-radius: 50%;
    background: rgba(255,255,255,0.28);
  }
  .label__facts {
    font-size: 11px;
    line-height: 1.3;
    letter-spacing: 0.3px;
  }
</style>
</head>
<body>
  <section class="label label--clear" style="left:145px">
    <div class="label__head">
      <h2 class="label__name">Liver<br>Clarity</h2>
      <p class="label__claim">Rejuvenating Cleanse<br>&amp; Detox Formula*</p>
    </div>
    <div class="label__band label__band--lilac">
      <div class="label__emblem" role="img" aria-label="Line drawing of a lotus flower"></div>
      <p class="label__facts">Dietary Supplement<br>120 Vegetable Capsules</p>
    </div>
  </section>

  <section class="label label--black" style="left:380px">
    <div class="label__head">
      <h2 class="label__name">Liver<br>Clarity</h2>
      <p class="label__claim">Rejuvenating Cleanse<br>&amp; Detox Formula*</p>
    </div>
    <div class="label__band label__band--lilac">
      <div class="label__emblem" role="img" aria-label="Line drawing of a lotus flower"></div>
      <p class="label__facts">Dietary Supplement<br>120 Vegetable Capsules</p>
    </div>
  </section>

  <section class="label label--clear" style="left:624px">
    <div class="label__head">
      <h2 class="label__name">Tummy<br>Clarity</h2>
      <p class="label__claim">Oxygenating Colon<br>Cleanse*</p>
    </div>
    <div class="label__band label__band--peach">
      <div class="label__emblem" role="img" aria-label="Line drawing of a rose"></div>
      <p class="label__facts">Dietary Supplement<br>90 Vegetable Capsules</p>
    </div>
  </section>

  <section class="label label--black" style="left:859px">
    <div class="label__head">
      <h2 class="label__name">Tummy<br>Clarity</h2>
      <p class="label__claim">Oxygenating Colon<br>Cleanse*</p>
    </div>
    <div class="label__band label__band--peach">
      <div class="label__emblem" role="img" aria-label="Line drawing of a rose"></div>
      <p class="label__facts">Dietary Supplement<br>90 Vegetable Capsules</p>
    </div>
  </section>
</body>
</html>
```